Roofing Company needs Business card design

We need a business card design for our roofing contracting company. We do Residential and commercial roofing. Design need to be modern, professional and clean. The design should communicate quality and professionalism. We would like to have rounded corners, but open to your ideas.
Company Name: Kestrel roofing Solutions
Company Address: (dummy text)
Name on business card: (dummy text)
And following lines:
Storm damage specialists
commercial & residential
shingles, flat and metal roofs./
Open to background colors.
I have ai. and eps files of logo if needed.
just let me know.
Target Market(s)
Mostly residential customers but we do commercial too.
Industry/Entity Type
Roofing
Look and feel

```html
<!DOCTYPE html>
<html lang="en">
<head>
<meta charset="utf-8">
<title>Kestrel Roofing Solutions – Business Card</title>
<link href="https://fonts.googleapis.com/css2?family=Questrial&display=swap" rel="stylesheet">
<style>
  :root {
    --backdrop: #c9cacc;
    --card-white: #ffffff;
    --card-black: #0d0d0e;
    --ink: #111111;
    --brand-red: #d4202a;
    --brand-orange: #f0652a;
    --tagline-orange: #f2662e;
  }
  * { box-sizing: border-box; margin: 0; padding: 0; }
  html, body {
    width: 1200px; height: 900px; overflow: hidden;
    background: var(--backdrop);
    font-family: "Questrial", "Century Gothic", sans-serif;
  }
  .canvas {
    position: relative; width: 1200px; height: 900px;
    display: flex; align-items: center; justify-content: center; gap: 44px;
  }
  .card {
    position: relative; width: 530px; height: 310px;
    border-radius: 30px; overflow: hidden;
  }
  /* front */
  .card-front { background: var(--card-white); }
  .holder {
    position: absolute; top: 22px; right: 36px; text-align: right;
  }
  .holder-name { color: var(--brand-red); font-size: 24px; line-height: 1.1; letter-spacing: 0.3px; }
  .holder-role { color: var(--ink); font-size: 15px; margin-top: 3px; }
  .company-name {
    position: absolute; left: 26px; top: 92px; white-space: nowrap;
    color: var(--brand-red); font-size: 22px; line-height: 1; letter-spacing: 0.6px;
    text-transform: uppercase;
  }
  .company-name .mark {
    display: inline-block; width: 13px; height: 13px; background: var(--brand-red);
    margin-right: 9px; vertical-align: 2px;
  }
  .contact-list {
    position: absolute; left: 24px; top: 150px; list-style: none;
    color: var(--ink); font-size: 15px; line-height: 20px;
  }
  .contact-list li { display: flex; align-items: flex-start; gap: 7px; }
  .contact-list svg { width: 13px; height: 13px; margin-top: 3px; flex: none; fill: var(--brand-red); }
  .base-band {
    position: absolute; left: 0; right: 0; bottom: 0; height: 36px;
    background: var(--card-black);
    border-top: 3px solid var(--brand-red);
  }
  .base-band::before {
    content: ""; position: absolute; left: 0; right: 0; top: -9px; height: 6px;
    background: linear-gradient(90deg, #ffffff 0%, var(--brand-orange) 60%, var(--brand-red) 100%);
    opacity: 0.35;
  }
  /* back */
  .card-back {
    background: radial-gradient(ellipse at 50% 40%, #262627 0%, var(--card-black) 75%);
    display: flex; flex-direction: column; align-items: center; justify-content: center; gap: 14px;
    padding-bottom: 40px;
  }
  .tagline { color: var(--tagline-orange); font-size: 18px; letter-spacing: 0.3px; }
</style>
</head>
<body>
  <main class="canvas">
    <section class="card card-front" aria-label="Business card front">
      <div class="holder">
        <p class="holder-name">Dana Hollis</p>
        <p class="holder-role">Manager</p>
      </div>
      <p class="company-name"><span class="mark"></span>Kestrel roofing Solutions</p>
      <ul class="contact-list">
        <li>
          <svg viewBox="0 0 16 16"><path d="M3.5 1l2.5 3-1.4 1.6a9 9 0 0 0 5.8 5.8L12 10l3 2.5-1.6 2.3C7.5 15 1 8.5 1.2 2.6z"/></svg>
          <span>1584 302 741</span>
        </li>
        <li>
          <svg viewBox="0 0 16 16"><path d="M1 3h14v10H1zM2 4l6 5 6-5v1.3L8 10.3 2 5.3z" fill-rule="evenodd"/></svg>
          <span>info@kestrelroofing.com</span>
        </li>
        <li>
          <svg viewBox="0 0 16 16"><path d="M8 1a7 7 0 1 0 0 14A7 7 0 0 0 8 1zm0 1.4c.9 1.2 1.5 2.8 1.6 4.6H6.4C6.5 5.2 7.1 3.6 8 2.4zM2.5 7h2.5c.1 1.7.5 3.3 1.2 4.5A5.6 5.6 0 0 1 2.5 9zM11 7h2.5a5.6 5.6 0 0 1-3.7 4.5c.7-1.2 1.1-2.8 1.2-4.5zM6.4 9h3.2c-.1 1.8-.7 3.4-1.6 4.6-.9-1.2-1.5-2.8-1.6-4.6z"/></svg>
          <span>www.kestrelroofing.com</span>
        </li>
        <li>
          <svg viewBox="0 0 16 16"><path d="M8 1.5L1 8h2v6.5h4v-4h2v4h4V8h2z"/></svg>
          <span>PO Box 40518,kestrel street<br>AL 36210,canada</span>
        </li>
      </ul>
      <div class="base-band"></div>
    </section>

    <section class="card card-back" aria-label="Business card back">
      <p class="tagline">Storm damage specialists</p>
      <p class="tagline">commercial &amp; residential</p>
      <p class="tagline">shingles, flat and metal roofs</p>
    </section>
  </main>
</body>
</html>
```